WEBSITE & LOGO for MEDICAL CILINC

BRAND NAME ( SOLVANE) Medical clinic for intravenous (IV) vitamin hydration and wellness therapy. range of signature infusions and boosters are targeted at preventative health and wellness – essentially replenishing your body with the fluids and vitamins it needs to be in tip-top condition.

Blood testing
laboratory analysis
IV therapy
IV infusion drips
phlebotomy services
nurses for Home care services
Patient repatriation services to their countries
Hire of medical equipments including beds and wheel chairs

www.quorbix.com
www.pelmaclinic.com
http://fonzelvo.co.uk

All adults
18+ women and men.

No black color in the background
DNA double helix image should to be implemented in the design and logo.
the website should be easy to be used so the clients can add to the shopping cart
- select treatment or drips
- supplement
- book nurses
- book home visit
- book nurse for international home care journey

Colors
86cae7
33b8a4
e4daeb
f9d9e8
fefafc
fbd2d3
eee9f4
85acd3
0455a3

Requirements
Must have
• DNA Double helix in Java animation
injection icon for IV injection
Infusion Icon Bag for IV infusion
Analysis icon
phlebotomy services icon
Patient repatriation services icon
Hire of medical equipments icon

light background and water blue menu and buttons with highlights
Nice to have
• dynamic website where
IV injections scroll from side to side
IV infusion scroll from side to side.

```html
<!DOCTYPE html>
<html lang="en">
<head>
<meta charset="utf-8">
<title>Solvane – IV Wellness Clinic</title>
<link href="https://fonts.googleapis.com/css2?family=Arimo:wght@400;700&display=swap" rel="stylesheet">
<style>
:root{
  --teal:#0e7399;
  --teal-dark:#0a5e83;
  --teal-btn:#0d7fa6;
  --bar:#0b6a8c;
  --ink:#444c52;
  --light:#f3f6f7;
  --water:#86cae7;
  --white:#ffffff;
}
*{box-sizing:border-box;margin:0;padding:0}
html,body{width:1200px;height:4237px;overflow:hidden;background:var(--white)}
body{font-family:"Arimo",Arial,sans-serif;color:var(--ink)}
.page{position:relative;width:1200px;height:4237px;overflow:hidden}
.abs{position:absolute}
.ph{position:absolute}
.btn{position:absolute;display:flex;align-items:center;justify-content:center;border-radius:20px;font-size:15px;background:linear-gradient(90deg,#0b6f94,#1596be);color:#fff;box-shadow:0 2px 4px rgba(0,0,0,.15)}
.btn.ghost{background:#fff;color:var(--teal);border:1.5px solid var(--teal-btn);box-shadow:none}
h2.section-title{position:absolute;color:var(--teal);font-weight:700;font-size:32px}
.body-text{position:absolute;font-size:14px;line-height:19px;text-align:justify;color:var(--ink)}

/* top bar */
.topbar{left:0;top:0;width:1200px;height:30px;background:linear-gradient(90deg,#0d5f80,#0e7a9d);color:#fff;font-size:13px}
.topbar span{position:absolute;top:8px}
.dot{position:absolute;width:12px;height:12px;border-radius:50%;background:#fff}
/* nav */
.nav{left:0;top:30px;width:1200px;height:70px;background:#fff;box-shadow:0 1px 3px rgba(0,0,0,.08)}
.brand{position:absolute;display:flex;align-items:center;gap:8px;font-weight:700;color:var(--teal)}
.brand i{display:block;border-radius:50%;background:var(--teal)}
.nav .links{position:absolute;left:293px;top:33px;font-size:15px;color:#333}
.nav .links span{position:absolute;white-space:nowrap}
/* hero */
.hero{left:0;top:100px;width:1200px;height:571px;background:radial-gradient(ellipse at 40% 40%,#5fb8e6 0%,#1a7cc0 40%,#0a3d7a 100%)}
.hero h1{position:absolute;left:0;width:1200px;top:222px;text-align:center;color:#fff;font-size:54px;font-weight:700;text-shadow:0 3px 6px rgba(0,0,0,.45)}
.hero .explore{position:absolute;left:529px;top:316px;width:138px;height:43px;border-radius:22px;background:#fff;color:var(--teal);font-size:15px;display:flex;align-items:center;justify-content:center}
.hero .pager{position:absolute;top:530px;width:13px;height:13px;border-radius:50%;border:2px solid #fff}
/* services */
.service{position:absolute;width:255px}
.service svg{display:block}
.service h3{font-weight:400;font-size:20px;color:var(--teal);margin:14px 0 12px}
.service h3.plain{color:#444}
.service p{font-size:14px;line-height:19px;text-align:justify}
/* carousel */
.carousel{left:0;top:1970px;width:1200px;height:438px;background:var(--light)}
.drip{position:absolute}
.drip .syringe{position:absolute;left:0;top:0;width:42px;height:450px;border-radius:6px;background:linear-gradient(180deg,#e9eef0 0%,#9dd27f 24%,#d8dde0 30%,#f4f6f7 60%,#b8c0c4 100%)}
.drip .hex{position:absolute;left:38px;top:171px}
.drip .hex span{position:absolute;left:0;top:0;width:204px;height:240px;display:flex;align-items:center;justify-content:center;color:#fff;font-weight:700;font-size:20px}
/* footer */
.footer{left:0;top:3768px;width:1200px;height:469px;background:var(--teal-dark);color:#fff}
.footer h4{position:absolute;top:112px;font-size:14px;font-weight:700;letter-spacing:.3px}
.footer .link{position:absolute;font-size:14px}
.footer .soc{position:absolute;top:256px;width:16px;height:16px;border-radius:50%;background:#fff}
</style>
</head>
<body>
<div class="page">

  <!-- top bar -->
  <div class="abs topbar">
    <svg class="abs" style="left:175px;top:8px" width="14" height="14" viewBox="0 0 24 24"><path fill="#fff" d="M6.6 10.8a15 15 0 0 0 6.6 6.6l2.2-2.2c.3-.3.7-.4 1-.2 1.1.4 2.3.6 3.6.6.6 0 1 .4 1 1V20c0 .6-.4 1-1 1A17 17 0 0 1 3 4c0-.6.4-1 1-1h3.5c.6 0 1 .4 1 1 0 1.3.2 2.5.6 3.6.1.3 0 .7-.2 1z"/></svg>
    <span style="left:212px">(555) 010-4471</span>
    <svg class="abs" style="left:370px;top:9px" width="18" height="13" viewBox="0 0 18 13"><rect x="1" y="1" width="16" height="11" fill="none" stroke="#fff" stroke-width="1.6"/><path d="M1 1l8 6 8-6" fill="none" stroke="#fff" stroke-width="1.6"/></svg>
    <span style="left:410px">hello@solvanemail.com</span>
    <i class="dot" style="left:915px;top:9px"></i>
    <i class="dot" style="left:943px;top:9px"></i>
    <i class="dot" style="left:971px;top:9px"></i>
    <i class="dot" style="left:999px;top:9px"></i>
  </div>

  <!-- nav -->
  <div class="abs nav">
    <div class="brand" style="left:87px;top:22px;font-size:17px"><i style="width:24px;height:24px"></i>SOLVANE</div>
    <div class="links">
      <span style="left:0">ABOUT</span>
      <span style="left:103px">DISCOVER</span>
      <span style="left:235px">IV THERAPY</span>
      <span style="left:378px">IV INFUSIONS</span>
      <span style="left:533px">GENETICS</span>
    </div>
    <div class="btn" style="left:993px;top:20px;width:119px;height:36px">Book Now</div>
  </div>

  <!-- hero -->
  <section class="abs hero" role="img" aria-label="Glowing blue DNA double helix strands in a molecular scene">
    <h1>Select Treatment or Drips</h1>
    <div class="explore">EXPLORE</div>
    <i class="pager" style="left:570px;background:#fff"></i>
    <i class="pager" style="left:592px"></i>
    <i class="pager" style="left:615px"></i>
  </section>

  <!-- about -->
  <h2 class="section-title" style="left:87px;top:736px">About Us</h2>
  <p class="body-text" style="left:87px;top:817px;width:420px">Live your life beyond limits with the help of wellness and recovery therapies that are tailored to your needs. Our signature IV therapies and vitamin injections will help you feel energized, invigorated, stimulated and refreshed.<br><br>Lead a healthy, balanced and enriched lifestyle with the help of our specially formulated injections and IV therapies. From minerals and antioxidants to vitamins</p>
  <div class="btn" style="left:87px;top:1026px;width:118px;height:36px;font-weight:700">Read More</div>
  <div class="ph" role="img" aria-label="Small decorative DNA double helix illustration" style="left:240px;top:1000px;width:95px;height:145px;border-radius:40px;background:linear-gradient(135deg,#bfe4f0,#7cc5dc)"></div>
  <div class="ph" role="img" aria-label="Photo of a nurse in a surgical cap and mask with a doctor behind her" style="left:603px;top:718px;width:564px;height:372px;border-radius:0 0 70px 0;background:linear-gradient(135deg,#cfd8dc 0%,#9fd4ea 45%,#e6ecef 100%)"></div>

  <!-- services -->
  <h2 class="section-title" style="left:0;width:1200px;text-align:center;top:1146px">Our Services</h2>

  <div class="service" style="left:128px;top:1236px">
    <svg width="44" height="58" viewBox="0 0 44 58" fill="none" stroke="#555" stroke-width="2"><rect x="6" y="4" width="30" height="40" rx="4"/><path d="M18 4V1h8v3M14 14h8M14 22h8M14 30h8M21 44v12"/></svg>
    <h3 class="plain">IV Infusion</h3>
    <p>IV infusion have been developed by a team of clinical professionals to deliver the vitamins, nutrients, fluids, electrolytes and antioxidants that your body needs.</p>
  </div>
  <div class="service" style="left:473px;top:1236px">
    <svg width="70" height="64" viewBox="0 0 70 64" fill="none" stroke="#555" stroke-width="2"><path d="M50 6l12 12M56 12l-8 8M44 14l12 12L24 58 12 46z"/><path d="M12 46L2 62M24 30l6 6M30 24l6 6"/></svg>
    <h3>IV Injection</h3>
    <p>IV injection have been developed by a team of clinical professionals to deliver the vitamins, nutrients, fluids, electrolytes and antioxidants that your body needs.</p>
  </div>
  <div class="service" style="left:819px;top:1236px">
    <svg width="64" height="64" viewBox="0 0 64 64" fill="none" stroke="#555" stroke-width="2"><circle cx="28" cy="32" r="26"/><path d="M2 32h52M28 6c-10 10-10 42 0 52M28 6c10 10 10 42 0 52"/><path d="M44 14l16-8-6 16"/></svg>
    <h3>Patient repatriation</h3>
    <p>patient repartriation have been developed by a team of clinical professionals to deliver the vitamins, nutrients, fluids, electrolytes and antioxidants that your body needs.</p>
  </div>

  <div class="service" style="left:128px;top:1537px">
    <svg width="58" height="58" viewBox="0 0 58 58" fill="none" stroke="#555" stroke-width="2"><rect x="2" y="12" width="54" height="42" rx="3"/><path d="M20 12V4h18v8M24 24h10v8h8v10h-8v8H24v-8h-8V32h8z"/></svg>
    <h3>Medical Equipments</h3>
    <p>Medical equipments have been developed by a team of clinical professionals to deliver the vitamins, nutrients, fluids, electrolytes and antioxidants that your body function</p>
  </div>
  <div class="service" style="left:473px;top:1537px">
    <svg width="62" height="58" viewBox="0 0 62 58" fill="none" stroke="#555" stroke-width="2"><path d="M6 54h50M14 46h34M22 8l10 22M18 10l8-4M30 30l-6 4"/><circle cx="48" cy="14" r="10"/><path d="M38 40c6 0 12-6 12-14"/></svg>
    <h3>Analysis</h3>
    <p>Analysing equipments have been developed by a team of clinical professionals to deliver the vitamins, nutrients, fluids, electrolytes and antioxidants that your body analysing</p>
  </div>
  <div class="service" style="left:819px;top:1537px">
    <svg width="62" height="58" viewBox="0 0 62 58" fill="none" stroke="#555" stroke-width="2"><path d="M6 30L31 8l25 22M12 26v30h38V26"/><rect x="25" y="40" width="12" height="16"/><path d="M27 22h8M31 18v8"/></svg>
    <h3>Home Cares</h3>
    <p>We care have been developed by a team of clinical professionals to deliver the vitamins, nutrients, fluids, electrolytes and antioxidants that from home.</p>
  </div>

  <div class="btn" style="left:541px;top:1810px;width:117px;height:36px">View More</div>

  <!-- drip carousel -->
  <section class="abs carousel">
    <svg class="abs" style="left:54px;top:200px" width="32" height="64" viewBox="0 0 32 64"><path d="M30 2L2 32l28 30" fill="none" stroke="#b5bcc0" stroke-width="2"/></svg>
    <svg class="abs" style="left:1114px;top:200px" width="32" height="64" viewBox="0 0 32 64"><path d="M2 2l28 30L2 62" fill="none" stroke="#b5bcc0" stroke-width="2"/></svg>
    <i class="abs" style="left:584px;top:423px;width:10px;height:3px;background:var(--teal-btn)"></i>
    <i class="abs" style="left:604px;top:423px;width:10px;height:3px;background:#c8d0d4"></i>
  </section>

  <div class="drip" style="left:156px;top:1899px">
    <div class="syringe" role="img" aria-label="Syringe illustration"></div>
    <div class="hex">
      <svg width="204" height="240" viewBox="0 0 204 240"><defs><linearGradient id="hexA" x1="0" y1="0" x2="1" y2="1"><stop offset="0" stop-color="#1a9ac4"/><stop offset="1" stop-color="#0d6a92"/></linearGradient></defs><polygon points="102,0 204,60 204,180 102,240 0,180 0,60" fill="url(#hexA)"/></svg>
      <span>GLUTATHIONE</span>
    </div>
  </div>
  <div class="drip" style="left:490px;top:1899px">
    <div class="syringe" role="img" aria-label="Syringe illustration"></div>
    <div class="hex">
      <svg width="204" height="240" viewBox="0 0 204 240"><polygon points="102,0 204,60 204,180 102,240 0,180 0,60" fill="url(#hexA)"/></svg>
      <span>VITAMIN B12</span>
    </div>
  </div>
  <div class="drip" style="left:824px;top:1899px">
    <div class="syringe" role="img" aria-label="Syringe illustration"></div>
    <div class="hex">
      <svg width="204" height="240" viewBox="0 0 204 240"><polygon points="102,0 204,60 204,180 102,240 0,180 0,60" fill="url(#hexA)"/></svg>
      <span>VITAMIN C</span>
    </div>
  </div>

  <!-- IV therapy -->
  <div class="ph" role="img" aria-label="Photo of a woman resting in a hospital bed" style="left:44px;top:2496px;width:449px;height:299px;border-radius:70px 0 0 0;background:linear-gradient(135deg,#f6ede3,#d9cbbd 60%,#b7c4b0);box-shadow:0 4px 14px rgba(0,0,0,.15)"></div>
  <div class="ph" role="img" aria-label="Close-up photo of an IV drip chamber" style="left:299px;top:2632px;width:296px;height:196px;border-radius:0 0 70px 0;background:linear-gradient(135deg,#ffffff,#cfdde6 50%,#6d8aa0);box-shadow:0 4px 14px rgba(0,0,0,.18)"></div>
  <h2 class="section-title" style="left:692px;top:2518px">IV Therapy</h2>
  <p class="body-text" style="left:692px;top:2586px;width:388px">Medical equipments have been developed by a team of clinical professionals to deliver the vitamins, nutrients, fluids, electrolytes and antioxidants that your body functionMedical equipments have been developed by a team of clinical professionals to deliver the vitamins, nutrients, fluids,</p>
  <div class="btn" style="left:692px;top:2742px;width:118px;height:36px">Book Now</div>
  <div class="btn ghost" style="left:829px;top:2742px;width:118px;height:36px">Learn More</div>

  <!-- home visit -->
  <h2 class="section-title" style="left:135px;top:2973px">Home visit</h2>
  <p class="body-text" style="left:135px;top:3041px;width:388px">Medical equipments have been developed by a team of clinical professionals to deliver the vitamins, nutrients, fluids, electrolytes and antioxidants that your body functionMedical equipments have been developed by a team of clinical professionals to deliver the vitamins, nutrients, fluids,</p>
  <div class="btn" style="left:135px;top:3198px;width:117px;height:36px">Book Now</div>
  <div class="btn ghost" style="left:273px;top:3198px;width:118px;height:36px">Learn More</div>
  <div class="ph" role="img" aria-label="Photo of a carer tending an elderly woman lying in bed at home" style="left:661px;top:2936px;width:449px;height:294px;border-radius:70px 0 70px 0;background:linear-gradient(135deg,#f3ece6,#e2d6cc 50%,#c9b6a8);box-shadow:0 4px 14px rgba(0,0,0,.15)"></div>

  <!-- book nurse -->
  <section class="abs" style="left:0;top:3411px;width:1200px;height:357px;background:linear-gradient(180deg,#f4fbfd 0%,#cdebf2 60%,#a9dce8 100%)"></section>
  <div class="ph" role="img" aria-label="Nurse in surgical cap and mask holding a syringe, beside a large DNA helix illustration" style="left:74px;top:3329px;width:460px;height:439px;border-radius:50% 50% 0 0 / 30% 30% 0 0;background:linear-gradient(160deg,#bfe3ef 0%,#5fbcd6 40%,#eef3f5 75%,#d7e3e8 100%)"></div>
  <h2 class="section-title" style="left:605px;top:3460px;line-height:39px">Book Nurse For<br>International Home Care Journey</h2>
  <p class="body-text" style="left:603px;top:3567px;width:502px">Medical equipments have been developed by a team of clinical professionals to deliver the vitamins, nutrients, fluids, electrolytes and antioxidants that your body functionMedical equipments have been developed by a team of clinical professionals to deliver the vitamins, nutrients, fluids,of clinical professionals</p>
  <div class="btn" style="left:602px;top:3691px;width:116px;height:36px">Book Now</div>

  <!-- footer -->
  <footer class="abs footer">
    <div class="brand" style="left:87px;top:112px;font-size:22px;color:#fff"><i style="width:30px;height:30px;background:#fff"></i>SOLVANE</div>
    <div class="link" style="left:87px;top:183px">Phone: 555 010 2288</div>
    <div class="link" style="left:87px;top:206px">Email: info@solvanemail.com</div>
    <i class="soc" style="left:87px"></i>
    <i class="soc" style="left:114px"></i>
    <i class="soc" style="left:147px"></i>
    <i class="soc" style="left:183px"></i>

    <h4 style="left:449px">MENUS</h4>
    <div class="link" style="left:449px;top:168px">Home</div>
    <div class="link" style="left:449px;top:204px">About Us</div>
    <div class="link" style="left:449px;top:240px">Services</div>
    <div class="link" style="left:449px;top:276px">News</div>
    <div class="link" style="left:449px;top:314px">Contact Us</div>

    <h4 style="left:641px">USEFUL LINKS</h4>
    <div class="link" style="left:641px;top:168px">IV Therapy</div>
    <div class="link" style="left:641px;top:204px">IV Infusion</div>
    <div class="link" style="left:641px;top:240px">Terms &amp; condition</div>
    <div class="link" style="left:641px;top:276px">Privacy Policy</div>

    <h4 style="left:876px">NEWSLETTER</h4>
    <div class="abs" style="left:876px;top:154px;width:235px;height:33px;border-radius:17px;background:#fff;color:#c3c8cb;font-size:12px;padding:10px 14px">Enter your E-mail</div>
    <div class="abs" style="left:876px;top:201px;width:84px;height:29px;border-radius:15px;border:1.5px solid #fff;font-size:14px;display:flex;align-items:center;justify-content:center">Submit</div>

    <i class="abs" style="left:0;top:386px;width:1200px;height:1px;background:rgba(255,255,255,.25)"></i>
    <div class="link" style="left:87px;top:414px;font-size:13px">© 2020 solvane. All rights reserved.</div>
  </footer>

</div>
</body>
</html>
```